New Logo and Packaging label for Sweet Chilli Sauce

We need a Logo Design for our business based in Sydney, Australia named Brovalt, and for the first product to launch which will be a Sweet Chilli Sauce. The logo and design has to be scalable to be used for other product additions over time.

The product will be distributed predominantly through growers markets and the web.

We do need a label that goes around a 250ml glass bottle (picture attached) and measures:
15cm tall and
6cm diameter at the widest point

To be included but not be limited to:
‘Brovalt’ logo that is developed
Sweet Chilli Sauce

Hand Made in Australia

250mL

Shake well
Refrigerate after opening

A section for ingredients, bar code and nutrition label

Target Market(s)

Foodies

Industry/Entity Type

Food Production

Logo Text

BROVALT

Colors

Designer to choose colors to be used in the design.

```html
<!DOCTYPE html>
<html lang="en">
<head>
<meta charset="utf-8">
<title>Brovalt Sweet Chilli Sauce Label</title>
<link href="https://fonts.googleapis.com/css2?family=Montserrat:wght@700;800&family=Yellowtail&display=swap" rel="stylesheet">
<style>
  :root {
    --hot-red: #ec1c24;
    --deep-red: #7a0f0f;
    --orange: #f26a1b;
    --amber: #f9a11b;
    --sun-yellow: #fff200;
    --white: #ffffff;
  }
  * { margin: 0; padding: 0; box-sizing: border-box; }
  html, body {
    width: 888px;
    height: 1200px;
    overflow: hidden;
  }
  .label {
    position: relative;
    width: 888px;
    height: 1200px;
    overflow: hidden;
    background:
      radial-gradient(ellipse 70% 60% at 50% 22%, rgba(255, 242, 0, 0.9) 0%, rgba(255, 242, 0, 0) 60%),
      linear-gradient(180deg, var(--hot-red) 0%, var(--orange) 30%, var(--amber) 62%, var(--sun-yellow) 88%, var(--sun-yellow) 100%);
  }
  .label::before {
    content: "";
    position: absolute;
    inset: 0;
    background: linear-gradient(90deg, rgba(236, 28, 36, 0.55) 0%, rgba(236, 28, 36, 0) 22%, rgba(236, 28, 36, 0) 78%, rgba(236, 28, 36, 0.55) 100%);
  }
  .brand-name {
    position: absolute;
    top: 170px;
    left: 0;
    width: 100%;
    text-align: center;
    font-family: "Montserrat", sans-serif;
    font-weight: 800;
    font-size: 124px;
    line-height: 1;
    color: var(--white);
  }
  .product-title {
    position: absolute;
    top: 448px;
    left: 0;
    width: 100%;
    z-index: 2;
    font-family: "Yellowtail", cursive;
    font-weight: 400;
    font-size: 138px;
    line-height: 118px;
    color: var(--white);
    text-shadow: 4px 4px 0 var(--deep-red);
  }
  .product-title span { display: block; }
  .title-sweet { padding-left: 300px; }
  .title-chilli { padding-left: 380px; }
  .title-sauce { padding-left: 236px; }
  .chilli-illustration {
    position: absolute;
    left: 92px;
    top: 760px;
    width: 720px;
    height: 236px;
    z-index: 1;
    border-radius: 50%;
    background: radial-gradient(ellipse at 55% 45%, #d81e1e 0%, #b01214 55%, rgba(176, 18, 20, 0) 72%);
  }
  .origin {
    position: absolute;
    top: 1030px;
    left: 0;
    width: 100%;
    text-align: center;
    font-family: "Montserrat", sans-serif;
    font-weight: 700;
    font-size: 41px;
    line-height: 1;
    color: var(--hot-red);
  }
  .volume-band {
    position: absolute;
    left: 0;
    bottom: 0;
    width: 100%;
    height: 98px;
    background: var(--hot-red);
    display: flex;
    align-items: center;
    justify-content: center;
    font-family: "Montserrat", sans-serif;
    font-weight: 700;
    color: var(--white);
  }
  .volume-number { font-size: 48px; line-height: 1; }
  .volume-unit { font-size: 34px; line-height: 1; }
</style>
</head>
<body>
  <main class="label">
    <h1 class="brand-name">Brovalt</h1>
    <h2 class="product-title">
      <span class="title-sweet">Sweet</span>
      <span class="title-chilli">Chilli</span>
      <span class="title-sauce">Sauce</span>
    </h2>
    <div class="chilli-illustration" role="img" aria-label="Illustration of a glossy red chilli pepper with a green stem"></div>
    <p class="origin">HAND MADE IN AUSTRALIA</p>
    <div class="volume-band">
      <span class="volume-number">250</span><span class="volume-unit">ML</span>
    </div>
  </main>
</body>
</html>
```